General Surgeon flyer to be distributed to GPs

I am a general surgeon and I would like to have a flyer designed aiming to introduce myself to GPs.

Name: Dr Tobias Vanterpool MD, FRACS
Address: Suite 4C, Brindle private hospital, 518 Cobbler Parade, Wantirna, VIC, 3152
T: (03) 9587 1062
F: (03) 9316 4471
E: referrals@lanternoperativeclinic.com.au
Website: www.lanternoperativeclinic.com.au

Tobias is a highly trained general surgeon, having completed extensive surgical training at Coralbay health, Fenwick and Thornleigh Health networks. He further specialized by completing a fellowship in Oesophagogastric and Bariatric Surgery at Larkspur Hospital Northgate, one of Victoria’s leading Upper GI surgical centres.

With expertise in both advanced laparoscopic and open surgical techniques, he performs a wide range of procedures involving the gastrointestinal system, abdominal wall hernias, as well as other major and minor general surgical operations. In addition to holding appointments at Coralbay Health, he also operates at Brindle and Quarrydale Private Hospitals.

Dr Vanterpool is committed to providing patient-centred care with a focus on surgical precision, safety, and long-term health outcomes.

He is also fluent in Farsi/Pesrian.
Outside of surgery, Tobias enjoys playings classical piano and spending time with his 6-year-old Bordoodle on long walks.

Upper GI & Bariatric Surgery:
Hiatus hernia repair, sleeve gastrectomy, gastric bypass
General Surgery conditions:
Gallbladder Surgery: Laparoscopic cholecystectomy
Hernia Repair: Laparoscopic and open surgery (inguinal,
umbilical, incisional)
Anorectal Procedures: Haemorrhoidectomy, haemorrhoid banding
Hand Surgery: Carpal tunnel release, Lymph Node Biopsy
Ingrown Toenail Surgery
Skin & Soft Tissue Surgery: Skin cancer removal, lipoma and
sebaceous cyst excision
Emergency Surgery: Laparotomy, Appendicectomy, bowel resection
Endoscopy: Diagnostic and therapeutic procedures

```html
<!DOCTYPE html>
<html lang="en">
<head>
<meta charset="utf-8">
<title>Dr Tobias Vanterpool – General Surgeon</title>
<link href="https://fonts.googleapis.com/css2?family=Questrial&family=Great+Vibes&display=swap" rel="stylesheet">
<style>
  :root{
    --teal:#5aa7b3;
    --panel:#e6e6e6;
    --ink:#2b2b2b;
    --white:#ffffff;
    --badge:#c9d5de;
    --hero-dark:#2f3336;
    --hero-mid:#5c6266;
  }
  *{margin:0;padding:0;box-sizing:border-box}
  html,body{width:849px;height:1200px;overflow:hidden;background:var(--white)}
  body{font-family:"Questrial",sans-serif;color:var(--ink)}
  .flyer{position:relative;width:849px;height:1200px;background:var(--white)}
  .top-band{position:absolute;left:0;top:0;width:849px;height:26px;background:var(--teal)}
  .hero{position:absolute;left:0;top:26px;width:849px;height:459px;overflow:hidden}
  .hero-photo{position:absolute;inset:0;
    background:
      radial-gradient(ellipse 260px 340px at 600px 300px, #d9dcde 0%, #aeb3b6 35%, rgba(90,96,100,0) 75%),
      radial-gradient(ellipse 120px 200px at 770px 330px, #bfc4c7 0%, rgba(90,96,100,0) 80%),
      linear-gradient(90deg, var(--hero-dark) 0%, #3c4144 45%, var(--hero-mid) 80%, #8b9194 100%)}
  .hero-title{position:absolute;left:40px;top:76px;width:400px;text-align:center;color:var(--white);
    font-weight:400;font-size:40px;line-height:48px;letter-spacing:.3px}
  .hero-tagline{position:absolute;left:72px;top:262px;color:var(--white);font-family:"Great Vibes",cursive;
    font-size:62px;line-height:56px;transform:rotate(-18deg);transform-origin:left top;white-space:nowrap}
  .hero-tagline span{display:block;padding-left:110px}
  .name-bar{position:absolute;left:0;top:374px;width:444px;height:53px;background:var(--teal);
    color:var(--white);font-size:22px;display:flex;align-items:center;padding-left:53px;letter-spacing:.3px}
  .bio{position:absolute;left:53px;top:527px;width:388px;height:506px;background:var(--panel);
    padding:16px 23px 0 26px;font-size:13.4px;line-height:18.4px;text-align:justify}
  .bio p{margin-bottom:18.4px}
  .services{position:absolute;left:475px;top:527px;width:325px;height:421px;background:var(--panel);
    padding:17px 25px 0 20px;font-size:13.4px;line-height:17.4px;text-align:justify}
  .services p{margin-bottom:17.4px}
  .contact{position:absolute;left:475px;top:978px;width:325px;height:181px;background:var(--teal);
    color:var(--white);padding:12px 8px 0 13px}
  .contact-name{font-size:15.5px;line-height:19px;padding-left:22px;margin-bottom:5px}
  .contact-row{display:flex;align-items:flex-start;font-size:13.4px;line-height:19px;white-space:nowrap}
  .contact-row svg{flex:0 0 14px;width:14px;height:14px;margin:2px 8px 0 0}
  .badge{position:absolute;background:var(--badge)}
  .badge-society{left:60px;top:1102px;width:72px;height:60px;border-radius:8px}
  .badge-college{left:171px;top:1123px;width:170px;height:36px;border-radius:4px}
  .clinic-mark{position:absolute;left:360px;top:1112px;display:flex;align-items:center;gap:6px;
    color:var(--teal);font-size:11px;line-height:13px;width:110px}
  .clinic-mark i{flex:0 0 18px;height:18px;border-radius:50%;background:var(--teal)}
</style>
</head>
<body>
<div class="flyer">
  <div class="top-band"></div>

  <section class="hero">
    <div class="hero-photo" role="img" aria-label="Smiling surgeon in a white coat with stethoscope and a colleague, in front of a bookshelf"></div>
    <h1 class="hero-title">Oesophagogastric and Bariatric Surgery</h1>
    <div class="hero-tagline">We provide<span>healthcare!</span></div>
    <div class="name-bar">Dr Tobias Vanterpool MD, FRACS</div>
  </section>

  <section class="bio">
    <p>Tobias is a highly trained general surgeon, having completed extensive surgical training at Coralbay health, Fenwick and Thornleigh Health networks. He further specialized by completing a fellowship in Oesophagogastric and Bariatric Surgery at Larkspur Hospital Northgate, one of Victoria’s leading Upper GI surgical centres.</p>
    <p>With expertise in both advanced laparoscopic and open surgical techniques, he performs a wide range of procedures involving the gastrointestinal system, abdominal wall hernias, as well as other major and minor general surgical operations. In addition to holding appointments at Coralbay Health, he also operates at Brindle and Quarrydale Private Hospitals.</p>
    <p>Dr Vanterpool is committed to providing patient-centred care with a focus on surgical precision, safety, and long-term health outcomes.</p>
    <p>He is also fluent in Farsi/Pesrian.</p>
    <p>Outside of surgery, Tobias enjoys playings classical piano and spending time with his 6-year-old Bordoodle on long walks.</p>
  </section>

  <section class="services">
    <p>Upper GI &amp; Bariatric Surgery:<br>Hiatus hernia repair, sleeve gastrectomy, gastric bypass</p>
    <p>General Surgery conditions:<br>Gallbladder Surgery: Laparoscopic cholecystectomy<br>Hernia Repair: Laparoscopic and open surgery (inguinal, umbilical, incisional)<br>Anorectal Procedures: Haemorrhoidectomy, haemorrhoid banding<br>Hand Surgery: Carpal tunnel release, Lymph Node Biopsy Ingrown Toenail Surgery<br>Skin &amp; Soft Tissue Surgery: Skin cancer removal, lipoma and sebaceous cyst excision</p>
    <p>Emergency Surgery:<br>Laparotomy, Appendicectomy, bowel resection</p>
    <p>Endoscopy:<br>Diagnostic and therapeutic procedures</p>
  </section>

  <section class="contact">
    <div class="contact-name">Dr Tobias Vanterpool MD, FRACS</div>
    <div class="contact-row">
      <svg viewBox="0 0 16 16" fill="none" stroke="#fff" stroke-width="1.2"><path d="M8 15s5-5 5-8.5A5 5 0 0 0 3 6.5C3 10 8 15 8 15z"/><circle cx="8" cy="6.5" r="1.8"/></svg>
      <span>Suite 4C, Brindle private hospital,<br>518 Cobbler Parade,<br>Ashcombe, VIC, 3187</span>
    </div>
    <div class="contact-row">
      <svg viewBox="0 0 16 16" fill="none" stroke="#fff" stroke-width="1.2"><circle cx="8" cy="8" r="7"/><path d="M5.5 4.5l1.5 1.5-1 1.2a5 5 0 0 0 2.8 2.8l1.2-1 1.5 1.5-1 1.2c-2.5 0-5.5-3-5.5-5.5z"/></svg>
      <span>(03) 9587 1062</span>
    </div>
    <div class="contact-row">
      <svg viewBox="0 0 16 16" fill="none" stroke="#fff" stroke-width="1.2"><circle cx="8" cy="8" r="7"/><rect x="4.5" y="6.5" width="7" height="4"/><path d="M6 6.5V4.5h4v2"/></svg>
      <span>(03) 9316 4471</span>
    </div>
    <div class="contact-row">
      <svg viewBox="0 0 16 16" fill="none" stroke="#fff" stroke-width="1.2"><circle cx="8" cy="8" r="7"/><rect x="4.5" y="5.5" width="7" height="5"/><path d="M4.5 5.5L8 8.5l3.5-3"/></svg>
      <span>referrals@lanternoperativeclinic.com.au</span>
    </div>
    <div class="contact-row">
      <svg viewBox="0 0 16 16" fill="none" stroke="#fff" stroke-width="1.2"><circle cx="8" cy="8" r="7"/><ellipse cx="8" cy="8" rx="3" ry="7"/><path d="M1 8h14M2.5 4.5h11M2.5 11.5h11"/></svg>
      <span>www.lanternoperativeclinic.com.au</span>
    </div>
  </section>

  <div class="badge badge-society" aria-hidden="true"></div>
  <div class="badge badge-college" aria-hidden="true"></div>
  <div class="clinic-mark"><i></i><span>Lantern Operative Clinic</span></div>
</div>
</body>
</html>
```